Infografik im Bereich Artikelbeschreibung für Onlineshop
Zielgruppe
Vertrieb von Saunaaustattung
Aufgabenstellung
Wird als Ergänzung für die Artikelbeschreibung im Webshop benötigt.
Ein Beispiel wo die Infografik platziert werden soll:
https://www.wolkenkessel-shop.de/Bilder/beispiel.jpg
Bildgröße ca. 1200 x 800 px
Als Hintergrund eventuell möglich teilweise oder ganz die Grafik mit den blauen Wassertropfen verwendbar?

```html
<!DOCTYPE html>
<html lang="de">
<head>
<meta charset="utf-8">
<title>Dampfgenerator – Ausstattungsmerkmale</title>
<link rel="stylesheet" href="https://fonts.googleapis.com/css2?family=Barlow+Semi+Condensed:wght@500;600&display=swap">
<style>
  :root {
    --blue-light: #3fc0ee;
    --blue-mid: #1d93da;
    --blue-deep: #166fbe;
    --blue-ring: #1a8fd6;
    --bg-top: #9cc7dc;
    --bg-mid: #5a9cc0;
    --bg-bottom: #2f78a6;
    --white: #ffffff;
    --line: #ffffff;
  }
  * { margin: 0; padding: 0; box-sizing: border-box; }
  html, body { width: 1200px; height: 800px; overflow: hidden; }
  body { font-family: "Barlow Semi Condensed", "Arial Narrow", sans-serif; color: var(--white); }

  .infographic { position: relative; width: 1200px; height: 800px; overflow: hidden; }

  .backdrop {
    position: absolute; inset: 0;
    background:
      radial-gradient(ellipse at 50% 20%, rgba(255,255,255,.35), transparent 60%),
      linear-gradient(180deg, var(--bg-top) 0%, var(--bg-mid) 55%, var(--bg-bottom) 100%);
  }

  .connectors { position: absolute; inset: 0; }

  .product-photo {
    position: absolute; left: 440px; top: 238px; width: 320px; height: 330px;
    border-radius: 6px;
    background: linear-gradient(135deg, #d9dcdf 0%, #b7bcc1 50%, #8d9399 100%);
  }

  /* side pills */
  .pill {
    position: absolute; height: 92px; display: flex; align-items: center;
    font-weight: 600; font-size: 23px; line-height: 1.2; text-transform: uppercase; letter-spacing: .3px;
  }
  .pill--left { left: 0; width: 326px; border-radius: 0 46px 46px 0; padding-left: 30px; }
  .pill--right { left: 858px; width: 342px; border-radius: 46px 0 0 46px; padding-left: 112px; }
  .pill__icon { position: absolute; right: 20px; top: 16px; width: 60px; height: 60px; }
  .pill__thumb {
    position: absolute; left: 6px; top: 6px; width: 80px; height: 80px; border-radius: 50%;
    border: 4px solid var(--white);
    background: radial-gradient(circle at 40% 40%, #e9ebee, #9aa1a8);
  }

  .tone-light { background: var(--blue-light); }
  .tone-mid { background: var(--blue-mid); }
  .tone-deep { background: var(--blue-deep); }

  /* top and bottom tabs */
  .tab {
    position: absolute; width: 110px; display: flex; flex-direction: column; align-items: flex-start;
    font-weight: 600; font-size: 10.5px; line-height: 1.3; text-transform: uppercase; padding: 0 10px;
  }
  .tab--top { top: 0; height: 136px; border-radius: 0 0 55px 55px; padding-top: 18px; }
  .tab--top .tab__icon { margin: 14px auto 0; width: 54px; height: 54px; }
  .tab--bottom { top: 652px; height: 148px; border-radius: 55px 55px 0 0; justify-content: flex-start; }
  .tab--bottom .tab__icon { margin: 20px auto 0; width: 60px; height: 60px; }
  .tab--bottom .tab__label { margin-top: 26px; font-size: 9.5px; }
  .tab svg, .pill__icon { stroke: var(--white); fill: none; stroke-width: 3; stroke-linecap: round; stroke-linejoin: round; }
</style>
</head>
<body>
<main class="infographic">
  <div class="backdrop" role="img" aria-label="Hintergrund: beschlagene Glasscheibe mit blauen Wassertropfen"></div>

  <svg class="connectors" width="1200" height="800" viewBox="0 0 1200 800" aria-hidden="true">
    <g stroke="var(--line)" stroke-width="5">
      <line x1="320" y1="180" x2="450" y2="245"/>
      <line x1="320" y1="290" x2="400" y2="315"/>
      <line x1="320" y1="400" x2="380" y2="400"/>
      <line x1="320" y1="515" x2="395" y2="490"/>
      <line x1="320" y1="630" x2="440" y2="555"/>
      <line x1="865" y1="175" x2="750" y2="240"/>
      <line x1="865" y1="285" x2="800" y2="315"/>
      <line x1="865" y1="400" x2="820" y2="400"/>
      <line x1="865" y1="515" x2="805" y2="490"/>
      <line x1="865" y1="625" x2="755" y2="560"/>
    </g>
    <circle cx="600" cy="402" r="230" fill="var(--blue-ring)"/>
    <circle cx="600" cy="402" r="208" fill="var(--white)"/>
  </svg>

  <div class="product-photo" role="img" aria-label="Produktfoto: Dampfgenerator im Edelstahlgehäuse mit Anschlüssen"></div>

  <!-- top tabs -->
  <div class="tab tab--top tone-mid" style="left:330px">
    <span class="tab__label">Thermoschutz</span>
    <svg class="tab__icon" viewBox="0 0 54 54"><path d="M27 5 L45 12 V27 C45 38 37 45 27 49 C17 45 9 38 9 27 V12 Z"/><path d="M27 16 V32"/><circle cx="27" cy="35" r="4"/></svg>
  </div>
  <div class="tab tab--top tone-light" style="left:466px">
    <span class="tab__label">Automatische Selbstreinigung</span>
    <svg class="tab__icon" viewBox="0 0 54 54"><path d="M40 6 L28 26"/><path d="M22 22 L34 30 L24 46 C16 44 10 38 8 32 Z"/></svg>
  </div>
  <div class="tab tab--top tone-mid" style="left:610px">
    <span class="tab__label">Kompakte Größe</span>
    <svg class="tab__icon" viewBox="0 0 54 54" style="stroke-width:2"><path d="M8 6 V46 H50"/><path d="M8 6 H46 V40" stroke-dasharray="3 3"/><text x="16" y="32" fill="#fff" stroke="none" font-size="13" font-family="Arial, sans-serif">cm²</text></svg>
  </div>
  <div class="tab tab--top tone-deep" style="left:757px">
    <span class="tab__label">Gerät kocht auf ca. 100 C° hoch</span>
    <svg class="tab__icon" viewBox="0 0 54 54"><circle cx="27" cy="27" r="22"/><circle cx="27" cy="27" r="8"/><path d="M11 11 L43 43"/></svg>
  </div>

  <!-- left pills -->
  <div class="pill pill--left tone-mid" style="top:113px">Inkludierte<br>Armoaauslassdüse
    <svg class="pill__icon" viewBox="0 0 60 60"><circle cx="30" cy="30" r="14"/><path d="M30 8 V14 M14 46 L18 42 M46 46 L42 42 M30 50 V54"/></svg>
  </div>
  <div class="pill pill--left tone-deep" style="top:230px">Kurze Aufheizzeit
    <svg class="pill__icon" viewBox="0 0 60 60" style="stroke-width:2.5"><path d="M10 22 A22 22 0 1 1 10 38"/><path d="M6 18 L10 24 L16 20"/><text x="19" y="30" fill="#fff" stroke="none" font-size="11" font-family="Arial, sans-serif">4 - 8</text><text x="20" y="42" fill="#fff" stroke="none" font-size="10" font-family="Arial, sans-serif">min</text></svg>
  </div>
  <div class="pill pill--left tone-mid" style="top:351px">Ansteuerung von bis<br>zu zwei Duftstoffen
    <svg class="pill__icon" viewBox="0 0 60 60" style="fill:#fff;stroke:none"><circle cx="18" cy="34" r="8"/><circle cx="36" cy="34" r="8"/><rect x="15" y="22" width="6" height="6"/><rect x="33" y="22" width="6" height="6"/></svg>
  </div>
  <div class="pill pill--left tone-light" style="top:475px">Optional<br>Steuerung per App
    <svg class="pill__icon" viewBox="0 0 60 60"><rect x="14" y="6" width="26" height="44" rx="4"/><path d="M30 30 V44 L46 48 V36 L34 32"/></svg>
  </div>
  <div class="pill pill--left tone-mid" style="top:596px">Elektronische<br>Entkalkung
    <svg class="pill__icon" viewBox="0 0 60 60"><path d="M18 26 H24 V8 H36 V26 H42 L30 48 Z"/></svg>
  </div>

  <!-- right pills -->
  <div class="pill pill--right tone-mid" style="top:114px">
    <div class="pill__thumb" role="img" aria-label="Detailfoto: Anschluss zum manuellen Entkalken"></div>Manuelles<br>Entkalken
  </div>
  <div class="pill pill--right tone-deep" style="top:228px">Gehäuse<br>Edelstahl<br>S304</div>
  <div class="pill pill--right tone-mid" style="top:350px">
    <div class="pill__thumb" role="img" aria-label="Detailfoto: Hochleistungs-Heizstab"></div>Hochleistungs-<br>heizstäbe
  </div>
  <div class="pill pill--right tone-light" style="top:471px">
    <div class="pill__thumb" role="img" aria-label="Detailfoto: elektronisches Abflussventil"></div>Elektronisches<br>Abflussventil
  </div>
  <div class="pill pill--right tone-mid" style="top:596px">Steuerdisplay<br>fliesenbündig<br>einbaubar</div>

  <!-- bottom tabs -->
  <div class="tab tab--bottom tone-light" style="left:330px">
    <svg class="tab__icon" viewBox="0 0 60 60"><path d="M20 38 C12 32 12 14 30 10 C48 14 48 32 40 38 Z"/><path d="M22 44 H38 M24 50 H36"/></svg>
    <span class="tab__label">Farblichtsteuerung</span>
  </div>
  <div class="tab tab--bottom tone-light" style="left:466px">
    <svg class="tab__icon" viewBox="0 0 60 60"><path d="M30 36 L44 14 L52 20 L38 42 Z"/><path d="M22 46 h1 M28 52 h1 M18 54 h1"/></svg>
    <span class="tab__label">Ansteuerung Salzsolevernebler</span>
  </div>
  <div class="tab tab--bottom tone-mid" style="left:610px">
    <svg class="tab__icon" viewBox="0 0 60 60"><path d="M26 8 H34 V36 A9 9 0 1 1 26 36 Z"/><path d="M38 14 H44 M38 22 H44 M38 30 H44"/></svg>
    <span class="tab__label">Verbrühschutz Abfluss</span>
  </div>
  <div class="tab tab--bottom tone-deep" style="left:757px">
    <svg class="tab__icon" viewBox="0 0 60 60"><circle cx="30" cy="30" r="4"/><path d="M30 26 C26 14 38 8 38 18 Z M34 32 C46 32 46 44 36 40 Z M26 32 C20 44 10 38 18 32 Z"/></svg>
    <span class="tab__label">Integrierte Abluftsteuerung</span>
  </div>
</main>
</body>
</html>
```